Fernvale Business Card Design

We are looking for a fresh business card design for our new logo. We would like a business card that is unique but friendly. We are in the window coverings business offering blinds, shutters and shades for homes.

Target Market(s)

Targeting the end-consumer

Industry/Entity Type

Business

Requirements
Must have
• Must have a dedicates space for a photo of our sales person. Must contain our new logo (attached).

```html
<!DOCTYPE html>
<html lang="en">
<head>
<meta charset="utf-8">
<title>Fernvale Business Card</title>
<link href="https://fonts.googleapis.com/css2?family=Source+Sans+3:wght@400&display=swap" rel="stylesheet">
<style>
  :root {
    --leaf-green: #8cc540;
    --slate: #6d6e71;
    --edge: #6b6b6b;
    --paper: #ffffff;
    --canvas: #ffffff;
  }
  * { box-sizing: border-box; margin: 0; padding: 0; }
  html, body {
    width: 1200px;
    height: 987px;
    overflow: hidden;
    background: var(--canvas);
    font-family: "Source Sans 3", "Myriad Pro", sans-serif;
    color: var(--slate);
  }
  .sheet { position: relative; width: 1200px; height: 987px; }

  .card {
    position: absolute;
    left: 269px;
    width: 659px;
    height: 365px;
    border: 1px solid var(--edge);
    border-radius: 19px;
    overflow: hidden;
    background: var(--paper);
  }
  .card--front { top: 67px; }
  .card--back { top: 493px; }

  /* Front */
  .front-band {
    position: absolute;
    left: 211px; top: 0;
    width: 448px; height: 100%;
    background: var(--leaf-green);
  }
  .brand-mark {
    position: absolute;
    left: 108px; top: 142px;
    width: 80px; height: 80px;
    background: var(--slate);
  }
  .brand-name {
    position: absolute;
    left: 218px; top: 135px;
    font-size: 70px;
    line-height: 1;
    font-weight: 400;
    color: var(--slate);
  }
  .brand-url {
    position: absolute;
    left: 224px; top: 324px;
    font-size: 22px;
    line-height: 1;
  }

  /* Back */
  .back-band {
    position: absolute;
    left: 0; top: 0;
    width: 329px; height: 100%;
    background: var(--leaf-green);
  }
  .photo-slot {
    position: absolute;
    left: 45px; top: 44px;
    width: 166px; height: 161px;
    background: var(--paper);
  }
  .back-brand {
    position: absolute;
    right: 44px; top: 40px;
    display: flex;
    align-items: center;
    gap: 10px;
  }
  .back-brand__mark {
    width: 26px; height: 26px;
    background: var(--slate);
  }
  .back-brand__name {
    font-size: 26px;
    line-height: 1;
    color: var(--slate);
  }
  .contact { position: absolute; left: 360px; }
  .contact__name { top: 137px; font-size: 24px; line-height: 1.1; }
  .contact__role { top: 166px; font-size: 18px; line-height: 1.1; }
  .contact__phone { top: 223px; font-size: 21px; line-height: 1.1; }
  .contact__email { top: 272px; font-size: 21px; line-height: 1.1; }
</style>
</head>
<body>
<main class="sheet">
  <section class="card card--front" aria-label="Card front">
    <div class="front-band"></div>
    <div class="brand-mark"></div>
    <h1 class="brand-name">Fernvale</h1>
    <p class="brand-url">www.fernvale.com</p>
  </section>

  <section class="card card--back" aria-label="Card back">
    <div class="back-band"></div>
    <div class="photo-slot" role="img" aria-label="Space for sales representative photo"></div>
    <div class="back-brand">
      <span class="back-brand__mark"></span>
      <span class="back-brand__name">Fernvale</span>
    </div>
    <p class="contact contact__name">Daniel Mwangi</p>
    <p class="contact contact__role">(Sales Representative)</p>
    <p class="contact contact__phone">0000 000 000</p>
    <p class="contact contact__email">aaaaaaaaa@mailbox.com</p>
  </section>
</main>
</body>
</html>
```